Harbor of Quiet Mornings book cover

Needing a book cover design and I have attached 3 sample covers for a starting point. I would like the design to use similar font as the sample cover along with a red and white theme. I would like a background image of broken shackles. On the back cover leave room for the author's bio and picture. The front cover and book details are below:
Book size: 6x9 or. 4.5x7
Title: Harbor of Quiet Mornings
Subtitle: Finding Calm Beneath Tall Lanterns at Dusk
Author: Noel Brantham
No spine is needed for the book due to it is a smaller book and the text will not fit. Yes, we are looking at every design and will choose winner on or before 4/20/2022

```html
<!DOCTYPE html>
<html lang="en">
<head>
<meta charset="utf-8">
<title>Harbor of Quiet Mornings — Book Cover</title>
<link rel="stylesheet" href="https://fonts.googleapis.com/css2?family=Cinzel:wght@400;500&display=swap">
<style>
  :root {
    --paper: #ffffff;
    --ink: #111111;
    --title-red: #e8242a;
    --steel-dark: #4a4a4a;
    --steel-mid: #9a9a9a;
    --steel-light: #e4e4e4;
  }
  * { margin: 0; padding: 0; box-sizing: border-box; }
  html, body {
    width: 800px;
    height: 1200px;
    overflow: hidden;
    background: var(--paper);
  }
  .cover {
    position: relative;
    width: 800px;
    height: 1200px;
    background: var(--paper);
    font-family: "Cinzel", serif;
    text-align: center;
    overflow: hidden;
  }
  .author {
    position: absolute;
    top: 36px;
    left: 0;
    width: 100%;
    font-size: 54px;
    font-weight: 400;
    color: var(--ink);
    letter-spacing: 1px;
    line-height: 1;
  }
  .title {
    position: absolute;
    top: 120px;
    left: 0;
    width: 100%;
    font-size: 104px;
    font-weight: 400;
    color: var(--title-red);
    line-height: 150px;
    letter-spacing: 0;
  }
  .title span, .subtitle span { display: block; }
  .subtitle {
    position: absolute;
    top: 590px;
    left: 0;
    width: 100%;
    font-size: 64px;
    font-weight: 400;
    color: var(--ink);
    line-height: 76px;
    z-index: 2;
  }
  .shackles-art {
    position: absolute;
    left: 50px;
    top: 820px;
    width: 700px;
    height: 320px;
    background:
      radial-gradient(ellipse 22% 40% at 18% 45%, var(--steel-dark) 0%, var(--steel-mid) 45%, rgba(255,255,255,0) 75%),
      radial-gradient(ellipse 18% 40% at 84% 40%, var(--steel-dark) 0%, var(--steel-mid) 45%, rgba(255,255,255,0) 75%),
      radial-gradient(ellipse 45% 12% at 50% 88%, var(--steel-mid) 0%, var(--steel-light) 50%, rgba(255,255,255,0) 80%);
    opacity: 0.85;
    z-index: 1;
  }
</style>
</head>
<body>
  <main class="cover">
    <p class="author">NOEL BRANTHAM</p>
    <h1 class="title">
      <span>HARBOR</span>
      <span>OF QUIET</span>
      <span>MORNINGS</span>
    </h1>
    <div class="shackles-art" role="img" aria-label="A pair of open iron shackles joined by a chain broken in the middle"></div>
    <h2 class="subtitle">
      <span>FINDING CALM</span>
      <span>BENEATH TALL</span>
      <span>LANTERNS</span>
      <span>AT DUSK</span>
    </h2>
  </main>
</body>
</html>
```